Label for Dog Nourishing CBD Balm

Dear Designers,

We are looking for a packaging expert to design our new Hydrating Balm for dogs which contain a relaxing hemp extract (CBD). The product is intended to be massaged on the dog’s paws to make them softer and promote the animal’s well-being :)

Our company is already selling various relaxing cat & dog products, and we would like this new design to reflect the same "style & feeling" as our current products (see attached ZIP file).

Technical aspects:
- The packaging is a 40ml aluminium jar (58mm x 23mm).
- We are looking to design 2 separate labels (one for the front, one for the back)
- The label dimensions should be : 50mm x 50mm
- Please follow technical guidelines from printer (see ZIP file).

Design aspects:
- The design should be compatible with our brand identity (i.e. fluffly, pure, relaxing, positive, clean & natural).
- People should understand what the product "is" and what the product "does" simply from looking at the design.
- The actual balm is white/yellow in color.
- Soft/rounded shapes are preferred.
- Please use our brand's colors (see typo & colors in ZIP file)
- Please use our brand's fonts (see typo & colors in ZIP file)
- Please use our company logo (see ZIP file).
- The design also needs to convey a strong sense of professionalism as we are an animal "healthcare" brand.
- If you want to include a dog picture, we would prefer you to use a picture of our official brand ambassador (see ZIP file).
- Only original work (no plagiarism will be accepted).

Please don't hesitate to send us a message if you have any questions about the brand, the product or the design requirements.

We look forward to seeing your designs & working on this together !

Thanks & regards,
Marcus

Target Market(s)

Dog owners

Font styles to use
Other font styles liked:
• See ZIP file

Requirements
Must have
• Brand fonts (see typo & colors in ZIP file)
Brand colors (see typo & colors in ZIP file)

```html
<!DOCTYPE html>
<html lang="en">
<head>
<meta charset="utf-8">
<title>LumaBalm Soothing Balm – Jar Labels</title>
<link rel="stylesheet" href="https://fonts.googleapis.com/css2?family=Montserrat:wght@400;500;600;700;800;900&family=Montserrat+Alternates:ital,wght@1,400&family=Roboto+Slab:wght@500&display=swap">
<style>
  :root {
    --backdrop: #4a4a4c;
    --teal: #3aa586;
    --forest: #1a3521;
    --ink: #1c1c1c;
    --white: #ffffff;
    --photo-light: #f2f1ef;
    --photo-mid: #d9d5d0;
  }
  * { margin: 0; padding: 0; box-sizing: border-box; }
  html, body {
    width: 1200px; height: 1142px; overflow: hidden;
    background: var(--backdrop);
    font-family: "Montserrat", sans-serif;
  }
  .canvas { position: relative; width: 1200px; height: 1142px; }

  .label {
    position: absolute; top: 301px;
    width: 540px; height: 540px;
    border-radius: 50%; overflow: hidden;
    background: var(--white);
  }
  .label--front { left: 30px; }
  .label--back { left: 630px; }
  .label__ring {
    position: absolute; inset: 0; border-radius: 50%;
    border: 18px solid var(--teal); z-index: 5; pointer-events: none;
  }

  /* Front label */
  .front__top-band { position: absolute; left: 0; top: 0; width: 540px; height: 110px; }
  .front__photo {
    position: absolute; left: 0; top: 96px; width: 262px; height: 259px;
    background: radial-gradient(ellipse at 55% 45%, var(--photo-light) 0%, var(--photo-mid) 100%);
    border-top-right-radius: 120px;
  }
  .brand {
    position: absolute; text-align: center;
    font-family: "Roboto Slab", serif; font-weight: 500; color: var(--forest);
  }
  .brand__tag {
    position: absolute; font-family: "Roboto Slab", serif; font-weight: 500;
    color: var(--teal); font-size: 11px;
  }
  .front .brand { left: 316px; top: 156px; width: 180px; font-size: 30px; }
  .front .brand__tag { left: 395px; top: 193px; }
  .front__product {
    position: absolute; right: 39px; top: 206px;
    font-family: "Montserrat Alternates", sans-serif; font-style: italic; font-weight: 400;
    font-size: 33px; color: var(--ink);
  }
  .front__title {
    position: absolute; right: 39px; top: 248px; text-align: right;
    font-weight: 900; font-size: 56px; line-height: 52px; letter-spacing: -1px;
    color: var(--forest);
  }
  .front__claims {
    position: absolute; left: 0; top: 355px; width: 540px; height: 53px;
    background: var(--forest); color: var(--white);
    font-weight: 700; font-size: 24px; line-height: 53px; text-align: center;
    padding-left: 12px;
  }
  .front__dose {
    position: absolute; left: 0; top: 408px; width: 540px; height: 132px;
    background: var(--teal); color: var(--forest);
    font-weight: 800; font-size: 28px; line-height: 56px; text-align: center;
  }
  .front__weight {
    position: absolute; left: 104px; top: 463px; width: 333px; height: 77px;
    background: var(--forest); color: var(--teal);
    clip-path: polygon(0 0, 100% 0, 91% 100%, 9% 100%);
    font-weight: 600; font-size: 34px; line-height: 62px; text-align: center;
  }

  /* Back label */
  .back .brand { left: 0; width: 540px; top: 68px; font-size: 28px; }
  .back .brand__tag { left: 300px; top: 103px; }
  .back__section { position: absolute; left: 40px; width: 460px; text-align: center; }
  .back__heading {
    color: var(--teal); font-weight: 500; font-size: 22px; line-height: 24px;
  }
  .back__text {
    color: var(--ink); font-weight: 500; font-size: 14px; line-height: 18.5px;
  }
  .back__section--about { top: 122px; }
  .back__section--use { top: 238px; }
  .back__section--ingredients { top: 340px; left: 24px; width: 492px; }
  .back__section--distributor { top: 405px; }
</style>
</head>
<body>
<main class="canvas">

  <section class="label label--front front" aria-label="Front label">
    <svg class="front__top-band" viewBox="0 0 540 110" aria-hidden="true">
      <path fill="var(--teal)" d="M0,0 H540 V68 H420 Q408,68 406,100 Q404,68 392,68 H170 Q140,68 120,40 Q105,18 80,18 H0 Z"/>
    </svg>
    <div class="front__photo" role="img" aria-label="Photo of the brand ambassador, a white Shar Pei dog in profile"></div>
    <div class="brand">LUMERRA</div>
    <div class="brand__tag">For Animals</div>
    <div class="front__product">LumaBalm</div>
    <h1 class="front__title">SOOTHING<br>BALM</h1>
    <div class="front__claims">REPAIR | NOURISH | PROTECT</div>
    <div class="front__dose">CBD 250MG | 0% THC</div>
    <div class="front__weight">40g</div>
    <div class="label__ring"></div>
  </section>

  <section class="label label--back back" aria-label="Back label">
    <div class="brand">LUMERRA</div>
    <div class="brand__tag">For Animals</div>

    <div class="back__section back__section--about">
      <h2 class="back__heading">EVERYDAY RELAXATION</h2>
      <p class="back__text">This balm repairs, nourishes and protects your<br>dog's sensitive skin. Its trusted multi-action formula<br>brings relief to fragile areas and soothes temporary irrations<br>(paw pads, elbows, etc.)</p>
    </div>

    <div class="back__section back__section--use">
      <h2 class="back__heading">RECOMMENDED USE:</h2>
      <p class="back__text">Rub a small amount of balm in the palm of your hand and<br>apply to sensitive areas as a daily care ritual. Repeat until the<br>product has been completely absorbed.</p>
    </div>

    <div class="back__section back__section--ingredients">
      <h2 class="back__heading">INGREDIENTS:</h2>
      <p class="back__text">Shea Butter, Beeswax, Coconut Oil, Hemp Extract (0% THC).</p>
    </div>

    <div class="back__section back__section--distributor">
      <h2 class="back__heading">Distributed by:</h2>
      <p class="back__text">LUMA EUROPE KFT.<br>Fenyő utca 14, 1075 Budapest<br>Hungary</p>
    </div>
    <div class="label__ring"></div>
  </section>

</main>
</body>
</html>
```